Wordpress theme customised please - for new ecommerce homewares website

Hi, we need a wordpress theme customised for a business that will sell tea towels (aka kitchen towels/dish cloths).
We do not have a website currently, but wish to launch using wordpress + woocommerce + "the shopfront" theme (c/- plumkestrel).
BACKGROUND RE THE BUSINESS
Our products are very stylish and will appeal to people who like owning gorgeous things - people who love cooking and/or decorating their home beautifully, or maybe they like travelling and/or buying presents for themselves and friends/family etc.
As they are typically used in people's kitchens, so "fresh" and "clean" is important - however the site must look very upmarket: timeless yet current, and classic yet simple, but not pretty, fussy or edgy.
We believe we have a great opportunity to leverage the "feel" of the product - cotton & linen fabric that has real texture to it, is tactile, natural, raw, real... in the photos used on the website, the backgrounds etc
Our logo is attached - a very dark grey colour was chosen, with white stripes, so that its neutral colouring would coordinate well with our suppliers' existing packaging. (We will represent a number of brands.)
BACKGROUND RE THIS PROJECT
We already know we want to use "the shopfront" theme by plumkestrel, but we need help customising the look of this theme so it works well with our logo, looks really striking and doesn't look like everyone else's ie "straight out of the box".
It appears these are the types of things that can be changed:
LAYOUT:
home page design concept (eg with a cascade carousel)
page design concept for eg About Us, Contact Us, FAQs
landing page design concept
header; light footer; dark footer
COLOURS & BACKGROUNDS & BORDERS & SEPARATORS:
main theme colour; accent colour; primary font colour
header background; light footer background colour; dark footer background colour; copyright bar background colour
dark footer widget title border; dark footer list separators and borders; dark footer/copyright bar separator styles
FONTS:
main navigation text colour; secondary navigation text colour; dark footer text colour; copyright bar text colour
main font; secondary font
LASTLY
Please don't hesitate to ask questions, request further information etc This is the first time we've posted a design project like this so it's tricky to know what other information you will need, so please just get in touch, ok!
Thanks so much for your interest in this project, and best wishes.

```html
<!DOCTYPE html>
<html lang="en">
<head>
<meta charset="utf-8">
<title>Linen Lane Goods</title>
<link href="https://fonts.googleapis.com/css2?family=Roboto:wght@400;500;700&family=Open+Sans:wght@400;600&display=swap" rel="stylesheet">
<style>
:root{
  --bar:#3b4053;
  --bar-line:#4d5368;
  --header:#2f3344;
  --footer:#2e3242;
  --footer-line:#41465a;
  --copyright:#3a3f52;
  --accent:#4b5d8f;
  --button:#6d87c4;
  --button-dark:#4d64a0;
  --ink:#2b2f3a;
  --body:#6e7280;
  --muted:#9ea3b5;
  --light:#e8e9f0;
  --white:#ffffff;
}
*{margin:0;padding:0;box-sizing:border-box}
html,body{width:943px;height:1200px;overflow:hidden}
body{position:relative;background:var(--white);font-family:"Open Sans",sans-serif;color:var(--body)}
.abs{position:absolute}
.top-bar{left:0;top:0;width:943px;height:30px;background:var(--bar);border-bottom:1px solid var(--bar-line)}
.top-bar .item{top:0;height:30px;line-height:30px;font:400 12px "Roboto",sans-serif;color:#b7bccc;padding:0 9px;border-right:1px solid var(--bar-line)}
.top-bar .or{display:inline-block;width:14px;height:14px;border-radius:50%;background:#2c3040;font-size:7px;line-height:14px;text-align:center;margin:0 6px;vertical-align:middle}
.tollfree{left:664px;top:3px}
.tollfree .phone{position:absolute;left:0;top:1px;width:22px;height:22px;border-radius:50%;background:#9aa0b4}
.tollfree small{position:absolute;left:28px;top:0;font:400 7px "Roboto",sans-serif;color:#9096aa;letter-spacing:.5px;white-space:nowrap}
.tollfree b{position:absolute;left:28px;top:7px;font:400 16px "Roboto",sans-serif;color:#b7bccc;white-space:nowrap;letter-spacing:.5px}
.header{left:0;top:31px;width:943px;height:292px;background:var(--header)}
.shade{left:0;top:323px;width:943px;height:90px;background:linear-gradient(#e4e5ec,#fff)}
.logo{left:128px;top:57px;font:500 20px "Roboto",sans-serif;color:var(--white);letter-spacing:2px}
.nav{top:56px;font-family:"Roboto",sans-serif}
.nav b{display:block;font:500 12px "Roboto",sans-serif;color:var(--white);letter-spacing:.5px}
.nav span{display:block;font-size:8px;color:#9ea3b5;margin-top:3px}
.nav-sep{top:58px;width:1px;height:26px;background:#454a5e}
.slider{left:126px;top:109px;width:692px;height:265px;background:#d8dbe8;border-radius:5px}
.slide-left{left:136px;top:119px;width:370px;height:246px;border-radius:4px 0 0 4px;background:linear-gradient(135deg,#ffffff,#e9eef3 50%,#d88a96 80%,#f2f2f2)}
.slide-right{left:506px;top:119px;width:303px;height:246px;border-radius:0 4px 4px 0;background:linear-gradient(90deg,#3b5b6a,#2d4a5a 40%,#e8e1cf 60%,#2f5767 80%,#ddd6c4)}
.caption{left:272px;top:292px;width:413px;height:48px;background:rgba(255,255,255,.82);text-align:center;line-height:48px;font:400 23px "Roboto",sans-serif;color:var(--ink)}
.caption strong{color:var(--accent);font-weight:500}
.dots{left:452px;top:394px}
.dots i{display:inline-block;width:11px;height:11px;border-radius:50%;background:#e7e8ee;border:1px solid #d0d2dc;margin-right:2px}
.dots i.on{background:radial-gradient(#4b5d8f 35%,#e7e8ee 40%)}
.rule{left:126px;width:692px;height:4px;background:var(--light)}
.section-title{background:var(--white);padding:0 4px;font:400 17px "Roboto",sans-serif;color:var(--ink);letter-spacing:.3px}
.section-title em{font-style:normal;color:var(--accent)}
.card{top:456px;width:212px;height:257px;border:1px solid #e0e2ea;border-radius:4px;background:var(--white);box-shadow:0 1px 3px rgba(0,0,0,.06);text-align:center}
.card .photo{height:152px;border-radius:4px 4px 0 0}
.card h3{font:500 15px "Roboto",sans-serif;color:var(--accent);margin-top:10px}
.card p{font-size:8.5px;line-height:12px;color:var(--body);padding:5px 16px 0}
.ribbon{right:-4px;top:-4px;width:72px;height:72px;overflow:hidden}
.ribbon span{position:absolute;left:-4px;top:20px;width:110px;transform:rotate(45deg);background:var(--button-dark);color:#fff;font:400 8px "Roboto",sans-serif;line-height:16px;text-align:center}
.btn{left:68px;top:235px;width:76px;height:24px;background:var(--button);color:#fff;font:500 10.5px "Roboto",sans-serif;line-height:24px;border-radius:2px}
.welcome-title{left:126px;top:775px;font:400 15px "Roboto",sans-serif;color:var(--ink)}
.welcome-title em{font-style:normal;color:var(--accent)}
.welcome-text{left:126px;top:802px;width:398px;font-size:8.5px;line-height:15.4px;text-align:justify;color:var(--body)}
.more{left:127px;top:937px;width:75px;height:18px;background:var(--button);border-radius:2px;color:#fff;font:500 8px "Roboto",sans-serif;line-height:18px;padding-left:5px}
.more i{position:absolute;right:0;top:0;width:17px;height:18px;background:#dfe3f0;border-radius:0 2px 2px 0}
.vline{left:552px;top:778px;width:4px;height:196px;background:var(--light)}
.quote{left:585px;top:807px;width:233px;height:121px;border:1px solid #e1e3ea;border-radius:3px;padding:12px 16px 0 34px;font-size:8.5px;line-height:15px;color:var(--body);text-align:justify}
.qmark{font:700 30px Georgia,serif;color:#dfe1e8}
.avatar{left:586px;top:943px;width:31px;height:31px;border-radius:50%;background:linear-gradient(#6a8fa0,#b08a70)}
.client-name{left:624px;top:945px;font:400 9.5px "Roboto",sans-serif;color:var(--accent)}
.client-role{left:624px;top:958px;font:400 8.5px "Roboto",sans-serif;color:var(--ink)}
.to-top{left:861px;top:982px;width:48px;height:48px;border-radius:50%;background:#f1f2f6;border:1px solid #cfd2dc;box-shadow:0 1px 4px rgba(0,0,0,.2);text-align:center;font:400 7px "Roboto",sans-serif;color:#7d8296;z-index:2}
.footer{left:0;top:1002px;width:943px;height:150px;background:var(--footer)}
.f-title{top:1030px;font:400 12px "Roboto",sans-serif;color:#fff}
.f-title:after{content:"";display:block;width:30px;height:2px;background:var(--button);margin-top:4px}
.f-list{list-style:none;font-size:8.5px;line-height:17px;color:#b6c2e8}
.f-list li:before{content:"• ";color:#8a90a4}
.f-sep{top:1028px;width:1px;height:106px;background:var(--footer-line)}
.contact li{display:flex;align-items:center;gap:8px;list-style:none;font-size:8.5px;color:#b6c2e8;height:18px}
.follow li{display:flex;align-items:center;gap:10px;list-style:none;font-size:8.5px;color:#b6c2e8;height:20px}
.follow li i{width:14px;height:14px;border-radius:50%;background:#e8e9f0}
.copyright{left:0;top:1152px;width:943px;height:48px;background:var(--copyright);border-top:1px solid var(--footer-line)}
.copy-logo{left:128px;top:1167px;font:500 14px "Roboto",sans-serif;color:#6f7589;letter-spacing:1.5px}
.copy-text{right:125px;top:1171px;font-size:8.5px;color:#9ea3b5}
</style>
</head>
<body>

<div class="abs top-bar">
  <div class="abs item" style="left:117px">Contact Us</div>
  <div class="abs item" style="left:186px;width:25px"></div>
  <div class="abs item" style="left:211px;width:25px"></div>
  <div class="abs item" style="left:236px;width:25px"></div>
  <div class="abs item" style="left:261px;padding-left:8px">
    <svg width="18" height="14" viewBox="0 0 18 14" style="vertical-align:-2px;margin-right:4px"><path d="M1 2h3l2 8h9l2-6H5" fill="none" stroke="#b7bccc" stroke-width="1.3"/><circle cx="7" cy="12.5" r="1.2" fill="#b7bccc"/><circle cx="14" cy="12.5" r="1.2" fill="#b7bccc"/></svg>Add to Card</div>
  <div class="abs item" style="left:358px;border-right:1px solid var(--bar-line)">Login<span class="or">or</span>Register</div>
  <div class="abs tollfree">
    <span class="phone"><svg width="22" height="22" viewBox="0 0 22 22"><path d="M8 6c-1 1-1 3 1 6s4 4 5 4l1.5-1.5-2-2-1 .8c-1-.5-2.3-2-2.6-3l.8-1-2-2z" fill="#3b4053"/></svg></span>
    <small>TOLL FREE NUMBER</small>
    <b>080 40 552100</b>
  </div>
</div>

<div class="abs header"></div>
<div class="abs shade"></div>

<div class="abs logo">LINEN LANE GOODS</div>
<div class="abs nav" style="left:440px"><b>PRODUCTS</b><span>Our Latest Products</span></div>
<div class="abs nav-sep" style="left:532px"></div>
<div class="abs nav" style="left:545px"><b>ABOUT US</b><span>Know About Us</span></div>
<div class="abs nav-sep" style="left:626px"></div>
<div class="abs nav" style="left:645px"><b>CONTACT US</b><span>Get In Touch</span></div>
<div class="abs nav-sep" style="left:742px"></div>
<div class="abs nav" style="left:760px"><b>FAQ</b><span>Ask Questions</span></div>

<div class="abs slider"></div>
<div class="abs slide-left" role="img" aria-label="Stack of folded striped and checked tea towels"></div>
<div class="abs slide-right" role="img" aria-label="Printed tea towels hanging from a wooden branch"></div>
<div class="abs caption">We are the <strong>best</strong> Product Seller</div>
<div class="abs dots"><i></i><i class="on"></i><i></i></div>

<div class="abs rule" style="top:423px"></div>
<div class="abs section-title" style="left:382px;top:415px">FEATURED <em>PRODUCTS</em></div>

<div class="abs card" style="left:126px">
  <div class="photo" role="img" aria-label="White kitchen towels with patterned borders beside pink tulips" style="background:linear-gradient(135deg,#c9c6ea,#f4f4f6 45%,#c9a5d8 75%,#e88fb5)"></div>
  <div class="abs ribbon"><span>New Product</span></div>
  <h3>Kitchen Towels</h3>
  <p>Morbi semper, odio ac molestie vulputate, enim odio ornare nisi, eget varius eros nisl a justo. Praesent purus diam.</p>
  <div class="abs btn">Read More</div>
</div>
<div class="abs card" style="left:365px">
  <div class="photo" role="img" aria-label="Woven dish cloths with purple and yellow check" style="background:linear-gradient(135deg,#ece9f2,#b8b0d8 40%,#f1e3a8 65%,#e9ebe4)"></div>
  <div class="abs ribbon"><span>New Product</span></div>
  <h3>Dish Cloths</h3>
  <p>Morbi semper, odio ac molestie vulputate, enim odio ornare nisi, eget varius eros nisl a justo. Praesent purus diam.</p>
  <div class="abs btn">Read More</div>
</div>
<div class="abs card" style="left:603px">
  <div class="photo" role="img" aria-label="Graphic print tea towels hanging on a rail" style="background:linear-gradient(90deg,#c9e1e6,#e7ecea 30%,#44506a 55%,#e5e8e6 75%,#c4dde2)"></div>
  <div class="abs ribbon"><span>New Product</span></div>
  <h3>Tea Towels</h3>
  <p>Morbi semper, odio ac molestie vulputate, enim odio ornare nisi, eget varius eros nisl a justo. Praesent purus diam.</p>
  <div class="abs btn">Read More</div>
</div>

<div class="abs rule" style="top:745px"></div>

<h2 class="abs welcome-title"><em>WELCOM TO</em> LINEN LANE GOODS</h2>
<p class="abs welcome-text">Lorem ipsum dolor sit amet, consectetur adipiscing elit. Proin non auctor justo. Aliquam erat volutpat. Mauris dui erat, semper ac molestie eu, pretium sed lectus. Aenean sollicitudin placerat ultrices. Quisque at dolor et erat dictum pulvinar. Nunc lobortis urna sed dolor lobortis semper. Donec ornare tristique justo, facilisis vehicula mauris consectetur et. Etiam a posuere lacus. Phasellus id justo convallis, aliquam libero sit amet, volutpat mi. Mauris suscipit tristique posuere. Pellentesque habitant morbi tristique senectus et netus et malesuada fames ac turpis egestas. Donec semper aliquam arcu, vel porttitor elit venenatis a. In eu nisl arcu. Praesent nec tristique felis, a rutrum sem.</p>
<div class="abs more">READ MORE<i><svg width="17" height="18" viewBox="0 0 17 18"><path d="M6 5l4 4-4 4" fill="none" stroke="#6d87c4" stroke-width="2"/></svg></i></div>

<div class="abs vline"></div>

<h2 class="abs welcome-title" style="left:584px"><em>CLIENTS</em> SPEAK</h2>
<div class="abs quote">
  <span class="abs qmark" style="left:12px;top:2px">“</span>
  Sed ut pers piciatis unde omnis iste natus error sit voluptatem accusa ntium dolore mque lauda ntium, totam rem aperiam, eaque ipsa quae ab illo inventore veritatis et quasi architecto beatae vitae dicta sunt explicabo.
  <span class="abs qmark" style="left:80px;top:82px">”</span>
</div>
<svg class="abs" style="left:596px;top:927px" width="16" height="10" viewBox="0 0 16 10"><path d="M0 0L2 10L12 0" fill="#fff" stroke="#e1e3ea"/><path d="M1 0h12" stroke="#fff" stroke-width="2"/></svg>
<div class="abs avatar" role="img" aria-label="Client portrait"></div>
<div class="abs client-name">Margot</div>
<div class="abs client-role">CEO Lorem Ipsum</div>

<div class="abs to-top"><svg width="20" height="14" viewBox="0 0 20 14" style="margin-top:8px"><path d="M10 1L19 12H1z" fill="#aeb2c2"/></svg><div>Go to Top</div></div>

<footer class="abs footer"></footer>
<div class="abs f-title" style="left:128px">Useful Links</div>
<ul class="abs f-list" style="left:128px;top:1058px"><li>Home</li><li>About Us</li><li>Products</li><li>Contact Us</li></ul>
<ul class="abs f-list" style="left:213px;top:1058px"><li>FAQ</li><li>Disclaimer</li><li>Pricing</li><li>Privacy Policy</li></ul>
<div class="abs f-sep" style="left:315px"></div>
<div class="abs f-title" style="left:351px">Products</div>
<ul class="abs f-list" style="left:351px;top:1058px"><li>Kitchen Towels</li><li>Dish Cloths</li><li>Tea Towels</li></ul>
<div class="abs f-sep" style="left:460px"></div>
<div class="abs f-title" style="left:500px">Contact Info</div>
<ul class="abs contact" style="left:500px;top:1059px">
  <li><svg width="10" height="12" viewBox="0 0 10 12"><path d="M5 0a4 4 0 0 0-4 4c0 3 4 8 4 8s4-5 4-8a4 4 0 0 0-4-4z" fill="#fff"/><circle cx="5" cy="4" r="1.5" fill="#2e3242"/></svg>Lorem Ipsum, Dolor Sit Amet, U.S.</li>
  <li><svg width="10" height="10" viewBox="0 0 10 10"><path d="M1 3c0-2 8-2 8 0v1H7V3H3v1H1zM2 5h6l1 4H1z" fill="#fff"/></svg>1400 21 43 65</li>
  <li><svg width="11" height="8" viewBox="0 0 11 8"><rect width="11" height="8" fill="#fff"/><path d="M0 0l5.5 4L11 0" fill="none" stroke="#2e3242"/></svg>info@linenlanegoods.com</li>
</ul>
<div class="abs f-sep" style="left:696px"></div>
<div class="abs f-title" style="left:728px">Follow Us</div>
<ul class="abs follow" style="left:728px;top:1058px">
  <li><i></i>Facenote</li>
  <li><i></i>Chirper</li>
  <li><i></i>Linkfold</li>
</ul>

<div class="abs copyright"></div>
<div class="abs copy-logo">LINEN LANE GOODS</div>
<div class="abs copy-text">Copyright 2013 by Linen Lane Goods - All Rights Reserved</div>

</body>
</html>
```